Create a moxiverse ad/campaign

Looking for a MV ad/campaign for a personal training MV page and online ads.
Use the attached pictures or others to create an appealing/energetic ad targeting clients who are looking to
-get fit for summer
-lose weight
-want to get back into their previous sport
-recovering from injury
-increase fitness

Not all of the above criteria must be included. These are just some examples.
Open to any ideas.

Looking forward to seeing your suggestions.

Thanks,

Omar

```html
<!DOCTYPE html>
<html lang="en">
<head>
<meta charset="UTF-8">
<title>MV Personal Training – Increase Fitness</title>
<link rel="stylesheet" href="https://fonts.googleapis.com/css2?family=Bebas+Neue&family=Oswald:wght@500;600&display=swap">
<style>
  :root {
    --backdrop: #e4e5e6;
    --brand-red: #c8141b;
    --brand-red-dark: #8e0a0f;
    --ink: #1f1f1f;
    --ink-soft: #2b2b2b;
    --white: #ffffff;
    --light-panel: rgba(255, 255, 255, 0.86);
    --photo-warm: #a86a3f;
    --photo-mid: #d9b48f;
    --photo-light: #efe7df;
  }
  html, body {
    margin: 0;
    padding: 0;
    width: 1063px;
    height: 1200px;
    overflow: hidden;
    background: var(--backdrop);
  }
  .ad-card {
    position: absolute;
    left: 126px;
    top: 224px;
    width: 825px;
    height: 825px;
    overflow: hidden;
    background: var(--white);
  }
  .hero-photo {
    position: absolute;
    inset: 0;
    background:
      radial-gradient(ellipse at 45% 55%, #e6c2aa 0%, rgba(230,194,170,0) 45%),
      linear-gradient(180deg, rgba(0,0,0,0) 70%, rgba(78,150,180,0.55) 100%),
      linear-gradient(100deg, var(--photo-warm) 0%, var(--photo-mid) 40%, var(--photo-light) 75%);
  }
  .light-panel {
    position: absolute;
    inset: 0;
    width: 825px;
    height: 825px;
  }
  .accent-ring {
    position: absolute;
    left: 0;
    top: 0;
    width: 825px;
    height: 825px;
  }
  .headline {
    position: absolute;
    left: 0;
    top: 0;
    margin: 0;
    font-family: "Bebas Neue", "Oswald", sans-serif;
    font-weight: 400;
  }
  .headline-top {
    position: absolute;
    left: 528px;
    top: 208px;
    font-size: 92px;
    line-height: 1;
    color: var(--brand-red);
    letter-spacing: 0.5px;
  }
  .headline-band {
    position: absolute;
    left: 530px;
    top: 299px;
    width: 295px;
    height: 90px;
    background: linear-gradient(90deg, var(--brand-red) 0%, var(--brand-red-dark) 100%);
  }
  .headline-bottom {
    position: absolute;
    left: 540px;
    top: 303px;
    font-size: 98px;
    line-height: 1;
    color: var(--white);
    letter-spacing: 0.5px;
  }
  .join-button {
    position: absolute;
    left: 578px;
    top: 433px;
    width: 203px;
    height: 48px;
    border-radius: 24px;
    background: var(--ink-soft);
    color: var(--white);
    font-family: "Bebas Neue", "Oswald", sans-serif;
    font-size: 32px;
    line-height: 50px;
    text-align: center;
    letter-spacing: 0.5px;
  }
  .dot-grid {
    position: absolute;
    left: 766px;
    top: 552px;
    width: 60px;
    height: 32px;
  }
  .contact {
    position: absolute;
    left: 560px;
    top: 636px;
    font-family: "Oswald", sans-serif;
    color: var(--ink);
  }
  .contact-row {
    position: absolute;
    left: 0;
    white-space: nowrap;
  }
  .contact-icon {
    position: absolute;
    width: 24px;
    height: 24px;
  }
  .call-label {
    left: 49px;
    top: 0;
    font-size: 17px;
    font-weight: 500;
    line-height: 1;
  }
  .call-number {
    left: 49px;
    top: 22px;
    font-size: 25px;
    font-weight: 600;
    line-height: 1;
  }
  .web-address {
    left: 49px;
    top: 58px;
    font-size: 21px;
    font-weight: 600;
    line-height: 1;
  }
</style>
</head>
<body>
  <main class="ad-card">
    <div class="hero-photo" role="img" aria-label="Photo of a woman in a sports top stretching in a cobra yoga pose on a blue mat in a sunny, warm living room with a brick wall"></div>

    <svg class="light-panel" viewBox="0 0 825 825" aria-hidden="true">
      <polygon points="535,0 825,0 825,825 305,825" fill="var(--light-panel)"/>
    </svg>

    <svg class="accent-ring" viewBox="0 0 825 825" aria-hidden="true">
      <circle cx="822" cy="62" r="82" fill="none" stroke="var(--brand-red)" stroke-width="6"/>
    </svg>

    <h1 class="headline">
      <span class="headline-top">Increase</span>
      <span class="headline-band"></span>
      <span class="headline-bottom">Fitness</span>
    </h1>

    <div class="join-button">Join Us</div>

    <svg class="dot-grid" viewBox="0 0 60 32" aria-hidden="true">
      <g fill="var(--brand-red)">
        <circle cx="4" cy="4" r="3.2"/><circle cx="14" cy="4" r="3.2"/><circle cx="24" cy="4" r="3.2"/><circle cx="34" cy="4" r="3.2"/><circle cx="44" cy="4" r="3.2"/><circle cx="54" cy="4" r="3.2"/>
        <circle cx="4" cy="15" r="3.2"/><circle cx="14" cy="15" r="3.2"/><circle cx="24" cy="15" r="3.2"/><circle cx="34" cy="15" r="3.2"/><circle cx="44" cy="15" r="3.2"/><circle cx="54" cy="15" r="3.2"/>
        <circle cx="4" cy="26" r="3.2"/><circle cx="14" cy="26" r="3.2"/><circle cx="24" cy="26" r="3.2"/><circle cx="34" cy="26" r="3.2"/><circle cx="44" cy="26" r="3.2"/><circle cx="54" cy="26" r="3.2"/>
      </g>
    </svg>

    <section class="contact">
      <svg class="contact-icon" style="left:8px; top:6px;" viewBox="0 0 24 24" aria-hidden="true">
        <path fill="var(--ink)" d="M6.6 10.8c1.4 2.8 3.8 5.1 6.6 6.6l2.2-2.2c.3-.3.7-.4 1-.2 1.1.4 2.3.6 3.6.6.6 0 1 .4 1 1V20c0 .6-.4 1-1 1C10.6 21 3 13.4 3 4c0-.6.4-1 1-1h3.5c.6 0 1 .4 1 1 0 1.3.2 2.5.6 3.6.1.3 0 .7-.2 1L6.6 10.8z"/>
      </svg>
      <span class="contact-row call-label">Call Now</span>
      <span class="contact-row call-number">+1555 20417</span>

      <svg class="contact-icon" style="left:9px; top:56px;" viewBox="0 0 24 24" aria-hidden="true">
        <g fill="none" stroke="var(--ink)" stroke-width="1.8">
          <circle cx="12" cy="12" r="9.5"/>
          <ellipse cx="12" cy="12" rx="4.2" ry="9.5"/>
          <line x1="2.5" y1="12" x2="21.5" y2="12"/>
          <path d="M4.2 7h15.6M4.2 17h15.6"/>
        </g>
      </svg>
      <span class="contact-row web-address">WWW.MOXIVERSEFIT.COM</span>
    </section>
  </main>
</body>
</html>
```